Design a business card Constest

You will be designing a business card for my business apartmentsvelmoria and touristinfovelmoria

You will design the business card with a front and a backside.

Front-side:
- Will have the logo of apartmentsvelmoria
- the contact details for: website, email, phone, whatsapp, sms (using icons, colored icons preferred)
- It will have the headline: "we've been expecting you"

Back-side:
- will have the logo touristinfovelmoria but then smaller
- website url
- a smaller text: "what brought us together?"
- 3 black lines where the user can write something on

Specifications:
- Created in Adobe Indesign
- Size dimensions: 85MM x 55MM
- You can use the template

About the mockup:
Please note that this is just a rough mock-up to show what type of things i want displayed on the card.
If you have any other good idea's you are always welcome to show me, be creative :)

```html
<!DOCTYPE html>
<html lang="en">
<head>
<meta charset="utf-8">
<title>Apartments Velmoria – Business Card</title>
<link href="https://fonts.googleapis.com/css2?family=Montserrat:wght@500;600&family=Lato:wght@400;700&display=swap" rel="stylesheet">
<style>
  :root {
    --bg: #6e6e6e;
    --card: #ffffff;
    --orange: #f26522;
    --green: #7ab648;
    --ink: #2b2b2b;
    --line: #3a3a3a;
  }
  * { margin: 0; padding: 0; box-sizing: border-box; }
  html, body { width: 1200px; height: 1200px; overflow: hidden; }
  body { background: var(--bg); position: relative; font-family: "Lato", sans-serif; }

  .card {
    position: absolute;
    left: 156px;
    width: 891px;
    height: 520px;
    background: var(--card);
    border-radius: 40px;
    overflow: hidden;
  }
  .card--back { top: 8px; }
  .card--front { top: 623px; }

  /* Back side */
  .brand-mark {
    position: absolute;
    display: flex;
    align-items: center;
    gap: 12px;
    font-family: "Montserrat", sans-serif;
    font-weight: 600;
    color: var(--orange);
    white-space: nowrap;
  }
  .brand-mark__dot {
    width: 18px; height: 18px; border-radius: 50%;
    background: var(--orange);
  }
  .card--back .brand-mark { left: 36px; top: 146px; font-size: 25px; }

  .back-site {
    position: absolute; left: 470px; top: 124px;
    display: flex; align-items: center; gap: 10px;
    font-size: 20px; color: var(--orange); letter-spacing: 0.5px;
  }
  .back-question {
    position: absolute; left: 441px; top: 155px;
    font-size: 26px; color: var(--green); letter-spacing: 1px;
  }
  .rule-accent {
    position: absolute; left: 37px; top: 219px; width: 811px;
    height: 2px; background: var(--orange);
  }
  .write-line {
    position: absolute; left: 37px; width: 811px; height: 2px; background: var(--line);
  }
  .write-line--1 { top: 338px; }
  .write-line--2 { top: 396px; }
  .write-line--3 { top: 455px; }

  /* Front side */
  .card--front .brand-mark {
    left: 0; right: 0; top: 186px; justify-content: center;
    font-size: 38px; letter-spacing: 0.5px;
  }
  .card--front .brand-mark__dot { width: 24px; height: 24px; border-radius: 3px; }

  .person {
    position: absolute; right: 480px; top: 310px; text-align: right;
  }
  .person__name {
    font-family: "Montserrat", sans-serif; font-weight: 500;
    font-size: 29px; color: var(--orange); letter-spacing: 0.5px;
  }
  .person__name .surname { color: var(--green); }
  .person__role { font-size: 18px; color: var(--ink); margin-top: 10px; }

  .divider {
    position: absolute; left: 447px; top: 292px; width: 2px; height: 114px;
    background: var(--orange);
  }
  .contacts {
    position: absolute; left: 473px; top: 285px; list-style: none;
  }
  .contacts li {
    display: flex; align-items: center; gap: 16px;
    height: 32px; font-size: 20px; color: var(--ink); letter-spacing: 0.5px;
  }
  .contacts svg { width: 18px; height: 18px; flex: none; }

  .tagline-band { position: absolute; left: 0; bottom: 0; width: 891px; height: 52px; }
  .tagline {
    position: absolute; left: 0; right: 0; bottom: 10px; text-align: center;
    font-size: 24px; color: #fff; letter-spacing: 0.8px;
  }
</style>
</head>
<body>

<section class="card card--back" aria-label="Card back">
  <div class="brand-mark"><span class="brand-mark__dot"></span>TOURISTINFOVELMORIA</div>
  <div class="back-site">
    <svg width="16" height="16" viewBox="0 0 16 16" aria-hidden="true">
      <circle cx="8" cy="8" r="7" fill="var(--orange)"/>
      <path d="M1 8h14M8 1c3 3 3 11 0 14M8 1c-3 3-3 11 0 14" stroke="#fff" stroke-width="1.2" fill="none"/>
    </svg>
    touristinfovelmoria.com
  </div>
  <p class="back-question">what brought us together?</p>
  <div class="rule-accent"></div>
  <div class="write-line write-line--1"></div>
  <div class="write-line write-line--2"></div>
  <div class="write-line write-line--3"></div>
</section>

<section class="card card--front" aria-label="Card front">
  <div class="brand-mark"><span class="brand-mark__dot"></span>APARTMENTSVELMORIA</div>

  <div class="person">
    <p class="person__name">MARCO <span class="surname">ELLERY</span></p>
    <p class="person__role">Manager</p>
  </div>

  <div class="divider"></div>

  <ul class="contacts">
    <li>
      <svg viewBox="0 0 18 18" aria-hidden="true"><path d="M4 1.5l3 3-1.8 2a10 10 0 0 0 6.3 6.3l2-1.8 3 3-2 2C7 16 2 11 1.9 3.5z" fill="var(--orange)"/></svg>
      +34 611 48 20 57
    </li>
    <li>
      <svg viewBox="0 0 18 18" aria-hidden="true"><circle cx="9" cy="9" r="7.5" fill="none" stroke="var(--orange)" stroke-width="2"/></svg>
      +34 611 48 20 57
    </li>
    <li>
      <svg viewBox="0 0 18 18" aria-hidden="true"><rect x="1" y="3.5" width="16" height="11" fill="var(--orange)"/><path d="M1 4l8 6 8-6" stroke="#fff" stroke-width="1.4" fill="none"/></svg>
      marcoelvm@mail.com
    </li>
    <li>
      <svg viewBox="0 0 18 18" aria-hidden="true"><circle cx="9" cy="9" r="8" fill="var(--orange)"/><path d="M1 9h16M9 1c3.5 3.5 3.5 12.5 0 16M9 1c-3.5 3.5-3.5 12.5 0 16" stroke="#fff" stroke-width="1.2" fill="none"/></svg>
      apartmentsvelmoria.com
    </li>
  </ul>

  <svg class="tagline-band" viewBox="0 0 891 52" aria-hidden="true">
    <rect x="0" y="6" width="891" height="46" fill="var(--orange)"/>
    <polygon points="220,0 664,0 720,52 168,52" fill="var(--green)"/>
    <polygon points="220,0 226,0 174,52 168,52" fill="#fff"/>
    <polygon points="658,0 664,0 720,52 714,52" fill="#fff"/>
  </svg>
  <p class="tagline">we've been expecting you</p>
</section>

</body>
</html>
```